KESTREL Communications Business Card- Belsa

Kestrel Integrated Communications is Corporate communications agency with more than 20 years of experience. We become part of the manegement team of our clients in other to improve their outcomes and grow the possitioning of their brand.
We are in Puerto Rico, latin caribbean island
Name: Maribelsa (Belsa) Ocampo
787-555-0148
bocampo@kestrelwing.example

Target Market(s)

finance and pharmaceutical companies

Industry/Entity Type

Business

Contact Information for Business Card

modern, edgy colorful and playfull like our logo

Requirements
Must have
• company logo
• name
• tel
• email

```html
<!DOCTYPE html>
<html lang="en">
<head>
<meta charset="utf-8">
<title>Kestrel Integrated Communications — Business Card</title>
<link rel="stylesheet" href="https://fonts.googleapis.com/css2?family=PT+Serif:wght@400;700&display=swap">
<style>
  :root {
    --page: #e8e8e8;
    --card: #ffffff;
    --charcoal: #303030;
    --orange: #e0643a;
    --brown: #3f2a08;
    --text: #2e2410;
  }
  * { margin: 0; padding: 0; box-sizing: border-box; }
  html, body { width: 1200px; height: 1200px; overflow: hidden; }
  body {
    background: var(--page);
    font-family: "PT Serif", Georgia, serif;
    color: var(--text);
    position: relative;
  }
  .card {
    position: absolute;
    left: 222px;
    width: 829px;
    height: 497px;
    background: var(--card);
    overflow: hidden;
  }
  .card--front { top: 93px; }
  .card--back { top: 644px; }
  .card__shapes { position: absolute; inset: 0; }

  .brand {
    position: absolute;
    display: flex;
    align-items: center;
    gap: 12px;
    transform: translate(-50%, -50%);
    white-space: nowrap;
  }
  .brand__dot {
    width: 16px; height: 16px;
    border-radius: 50%;
    background: var(--orange);
    flex: none;
  }
  .brand__name {
    font-weight: 700;
    color: var(--brown);
    line-height: 1.15;
    text-align: left;
  }
  .card--front .brand { left: 414px; top: 195px; }
  .card--front .brand__name { font-size: 34px; }
  .card--back .brand { left: 208px; top: 248px; }
  .card--back .brand__name { font-size: 24px; }

  .divider {
    position: absolute;
    left: 378px; top: 130px;
    width: 2px; height: 238px;
    background: var(--orange);
  }
  .contact { position: absolute; left: 434px; top: 156px; }
  .contact__name {
    font-size: 38px;
    font-weight: 700;
    color: var(--brown);
    letter-spacing: 0.5px;
    line-height: 1;
  }
  .contact__list { list-style: none; margin-top: 35px; }
  .contact__item {
    display: flex; align-items: center;
    font-size: 22px; line-height: 1;
    height: 32px; margin-bottom: 30px;
  }
  .contact__icon {
    width: 32px; height: 32px;
    border-radius: 5px;
    background: var(--orange);
    margin-right: 22px;
    flex: none;
    display: flex; align-items: center; justify-content: center;
  }
  .card__band {
    position: absolute;
    left: 0; right: 0; bottom: 0;
    height: 20px;
    background: var(--brown);
  }
</style>
</head>
<body>
  <section class="card card--front" aria-label="Business card front">
    <svg class="card__shapes" width="829" height="497" viewBox="0 0 829 497" aria-hidden="true">
      <polygon points="0,321 814,497 0,497" fill="var(--charcoal)"/>
      <polygon points="556,438 829,308 829,497" fill="var(--orange)"/>
    </svg>
    <div class="brand">
      <span class="brand__dot"></span>
      <span class="brand__name">Kestrel<br>Integrated Communications</span>
    </div>
  </section>

  <section class="card card--back" aria-label="Business card back">
    <div class="brand">
      <span class="brand__dot"></span>
      <span class="brand__name">Kestrel<br>Integrated<br>Communications</span>
    </div>
    <div class="divider"></div>
    <div class="contact">
      <h1 class="contact__name">Maribelsa Ocampo</h1>
      <ul class="contact__list">
        <li class="contact__item">
          <span class="contact__icon">
            <svg width="18" height="18" viewBox="0 0 24 24" aria-hidden="true">
              <path d="M6.6 10.8c1.4 2.8 3.8 5.1 6.6 6.6l2.2-2.2c.3-.3.7-.4 1-.2 1.1.4 2.3.6 3.6.6.6 0 1 .4 1 1V20c0 .6-.4 1-1 1C10.6 21 3 13.4 3 4c0-.6.4-1 1-1h3.5c.6 0 1 .4 1 1 0 1.3.2 2.5.6 3.6.1.3 0 .7-.2 1l-2.3 2.2z" fill="#fff"/>
            </svg>
          </span>
          787-555-0148
        </li>
        <li class="contact__item">
          <span class="contact__icon">
            <svg width="20" height="16" viewBox="0 0 20 16" aria-hidden="true">
              <rect x="1" y="1" width="18" height="14" fill="none" stroke="#fff" stroke-width="1.6"/>
              <path d="M1 1l9 8 9-8M1 15l6.5-6M19 15l-6.5-6" fill="none" stroke="#fff" stroke-width="1.6"/>
            </svg>
          </span>
          bocampo@kestrelwing.example
        </li>
      </ul>
    </div>
    <div class="card__band"></div>
  </section>
</body>
</html>
```